Creation of a book cover
Size : 14 x 20,5 cm (+ 5 mm bleed area at the top, bottom and right areas)
The Title is a French sentence which means “The heron dreaming on the cold roof of this empty station”. It’s a surrealistic title which has no link to the story.
AUTHOR : Mathieu Vorlange
TITLE : "Le héron rêvant sur le toit froid de cette gare vide »
PUBLISHER (AT THE BOTTOM OF THE PAGE) : Editions Parvenche
I send a PDF file with the kind of cover we have imagine, but you can propose something different. The glass and the fly can of course be used.

```html
<!DOCTYPE html>
<html lang="fr">
<head>
<meta charset="utf-8">
<title>Le héron rêvant sur le toit froid de cette gare vide — Mathieu Vorlange</title>
<link rel="stylesheet" href="https://fonts.googleapis.com/css2?family=Staatliches&family=Oswald:wght@600&family=Tinos&display=swap">
<style>
  :root {
    --stage: #e6e6e8;
    --paper-light: #f1ece2;
    --paper-mid: #e4dccd;
    --paper-edge: #cfc4b0;
    --band-brown: #7a4a2c;
    --title-cream: #eadfc6;
    --subtitle-navy: #142a3a;
    --ink-dark: #2b2a28;
    --publisher-cream: #e8dcc4;
    --glass-tone: #c9d3d2;
    --glass-deep: #8fa3a6;
  }
  html, body {
    margin: 0;
    padding: 0;
    width: 1200px;
    height: 882px;
    overflow: hidden;
    background: var(--stage);
  }
  .stage {
    position: relative;
    width: 1200px;
    height: 882px;
  }
  .book-cover {
    position: absolute;
    left: 320px;
    top: 31px;
    width: 560px;
    height: 820px;
    overflow: hidden;
    background:
      radial-gradient(ellipse at 50% 50%, var(--paper-light) 0%, var(--paper-mid) 65%, var(--paper-edge) 100%);
    box-shadow: 0 6px 18px rgba(0,0,0,0.18);
  }
  .cover-bands {
    position: absolute;
    inset: 0;
    width: 560px;
    height: 820px;
  }
  .author-name {
    position: absolute;
    top: 44px;
    left: 0;
    width: 100%;
    text-align: center;
    font-family: "Tinos", "Times New Roman", serif;
    font-size: 21px;
    letter-spacing: 1px;
    color: var(--ink-dark);
    margin: 0;
  }
  .book-title {
    position: absolute;
    top: 118px;
    left: 0;
    width: 100%;
    text-align: center;
    font-family: "Staatliches", "Impact", sans-serif;
    font-size: 86px;
    line-height: 1;
    letter-spacing: 3px;
    color: var(--title-cream);
    margin: 0;
  }
  .book-subtitle {
    position: absolute;
    top: 268px;
    left: 0;
    width: 100%;
    text-align: center;
    font-family: "Oswald", "Arial Narrow", sans-serif;
    font-weight: 600;
    font-size: 29px;
    line-height: 34px;
    color: var(--subtitle-navy);
    margin: 0;
  }
  .cover-illustration {
    position: absolute;
    left: 142px;
    top: 386px;
    width: 276px;
    height: 266px;
    border-radius: 10px 10px 40px 40px;
    background: linear-gradient(180deg, rgba(255,255,255,0.4) 0%, var(--glass-tone) 35%, var(--glass-deep) 100%);
  }
  .publisher-name {
    position: absolute;
    top: 728px;
    left: 0;
    width: 100%;
    text-align: center;
    font-family: "Tinos", "Times New Roman", serif;
    font-size: 19px;
    letter-spacing: 1px;
    color: var(--publisher-cream);
    margin: 0;
  }
</style>
</head>
<body>
<main class="stage">
  <article class="book-cover">
    <svg class="cover-bands" viewBox="0 0 560 820" aria-hidden="true">
      <polygon fill="var(--band-brown)" points="
        0,140 20,134 38,139 60,128 82,131 104,122 126,126 148,116 170,119 192,110 214,113 236,104 258,106
        280,98 302,101 324,93 346,95 368,88 390,90 412,83 434,86 456,79 478,81 500,76 522,78 544,72 560,73
        560,254 540,257 520,252 500,259 480,255 460,262 440,258 420,265 400,262 380,268 360,265 340,271
        320,268 300,274 280,271 260,277 240,274 220,279 200,277 180,281 160,279 140,284 120,281 100,286
        80,283 60,288 40,285 20,290 0,287" />
      <polygon fill="var(--band-brown)" points="
        0,722 20,716 42,720 64,712 86,715 108,707 130,710 152,702 174,705 196,698 218,700 240,693 262,696
        284,689 306,691 328,685 350,688 372,681 394,683 416,676 438,679 460,672 482,674 504,667 526,670
        546,663 560,664 560,820 0,820" />
    </svg>
    <p class="author-name">MATHIEU VORLANGE</p>
    <h1 class="book-title">LE HÉRON</h1>
    <p class="book-subtitle">RÊVANT SUR LE TOIT FROID<br>DE CETTE GARE VIDE</p>
    <div class="cover-illustration" role="img" aria-label="Illustration gravée d’un verre d’eau avec une mouche posée sur la surface"></div>
    <p class="publisher-name">ÉDITIONS PARVENCHE</p>
  </article>
</main>
</body>
</html>
```